Business Card Design

I would like a new business card design for an accounting firm that specializes in resolving clients tax problems. I want the card to give the impression that we are not your typical stodgy accounting firm, but at the same time we will get the job done.
Industry/Entity Type
Business
Contact Information for Business Card
Dorian T Welsby
Certified Public Accountant
38-27 52nd Street
Sunnyside, NY 11287
Tel: (718) 555-0142
Fax: (888) 555-0199
e-mail: dtwthecpa@ledgerpost.com
website: harborfilingreliefexperts.com

```html
<!DOCTYPE html>
<html lang="en">
<head>
<meta charset="utf-8">
<title>Dorian T. Welsby – Business Card</title>
<link rel="stylesheet" href="https://fonts.googleapis.com/css2?family=Playfair+Display:wght@700&family=Roboto+Condensed:wght@700&family=Open+Sans:wght@400&display=swap">
<style>
  :root {
    --page: #e9e6e1;
    --blue-light: #2b6db5;
    --blue-dark: #14488a;
    --yellow: #f4c313;
    --yellow-deep: #e0ab05;
    --white: #ffffff;
    --line: rgba(255,255,255,0.75);
  }
  * { margin: 0; padding: 0; box-sizing: border-box; }
  html, body {
    width: 1200px; height: 1022px; overflow: hidden;
    background: var(--page);
  }
  .card {
    position: absolute; left: 100px; top: 225px;
    width: 1000px; height: 571px;
    border-radius: 24px; overflow: hidden;
    background: linear-gradient(160deg, var(--blue-light) 0%, #1f5ca3 45%, var(--blue-dark) 100%);
    box-shadow: 0 10px 30px rgba(0,0,0,0.25);
  }
  .card__band { position: absolute; inset: 0; }
  .name-plate {
    position: absolute; left: 62px; top: 92px;
    width: 520px; height: 148px;
    border: 3px solid rgba(255,255,255,0.8);
    border-radius: 16px;
    background: rgba(255,255,255,0.08);
    display: flex; flex-direction: column; justify-content: center;
    padding-left: 34px;
  }
  .name-plate__name {
    font-family: "Playfair Display", serif; font-weight: 700;
    color: var(--white); font-size: 50px; letter-spacing: 4px;
    text-transform: uppercase; line-height: 1;
  }
  .name-plate__title {
    margin-top: 12px;
    font-family: "Roboto Condensed", sans-serif; font-weight: 700;
    color: var(--yellow); font-size: 24px; letter-spacing: 5px;
    text-transform: uppercase;
  }
  .divider {
    position: absolute; left: 62px; top: 290px;
    width: 740px; height: 2px; background: var(--line);
  }
  .address {
    position: absolute; left: 72px; top: 400px;
    font-family: "Open Sans", sans-serif; color: var(--white);
    font-size: 26px; line-height: 38px;
  }
  .contacts {
    position: absolute; right: 160px; top: 312px;
    list-style: none;
    font-family: "Open Sans", sans-serif; color: var(--white);
    font-size: 24px; line-height: 40px; text-align: right;
  }
  .contacts li { display: flex; justify-content: flex-end; align-items: center; gap: 12px; }
  .contacts svg { width: 20px; height: 20px; flex: none; }
</style>
</head>
<body>
  <main class="card">
    <svg class="card__band" viewBox="0 0 1000 571" aria-hidden="true">
      <path d="M900 0 H1000 V571 H900 V300 C900 270 880 262 862 250 C845 240 840 225 840 200 V0 Z" fill="var(--yellow)"/>
      <path d="M900 300 C900 270 880 262 862 250 C845 240 840 225 840 200" fill="none" stroke="var(--yellow-deep)" stroke-width="4"/>
      <g class="stripe-tab">
        <rect x="900" y="470" width="100" height="16" fill="var(--white)"/>
        <rect x="900" y="486" width="100" height="16" fill="var(--yellow)"/>
        <rect x="900" y="502" width="100" height="16" fill="var(--white)"/>
        <rect x="900" y="518" width="100" height="16" fill="var(--yellow)"/>
        <rect x="900" y="534" width="100" height="16" fill="var(--white)"/>
      </g>
    </svg>

    <div class="name-plate">
      <h1 class="name-plate__name">Dorian T. Welsby</h1>
      <p class="name-plate__title">Certified Public Accountant</p>
    </div>

    <div class="divider"></div>

    <address class="address">
      38-27 52nd Street<br>
      Sunnyside, NY 11287
    </address>

    <ul class="contacts">
      <li>(718) 555-0142
        <svg viewBox="0 0 20 20"><path d="M5 2 L8 6 L6.5 8 C7.5 10.5 9.5 12.5 12 13.5 L14 12 L18 15 L16 18 C9 18 2 11 2 4 Z" fill="var(--yellow)"/></svg>
      </li>
      <li>(888) 555-0199
        <svg viewBox="0 0 20 20"><rect x="5" y="2" width="10" height="5" fill="var(--yellow)"/><rect x="2" y="7" width="16" height="7" rx="1" fill="var(--yellow)"/><rect x="5" y="12" width="10" height="6" fill="var(--yellow)"/></svg>
      </li>
      <li>dtwthecpa@ledgerpost.com
        <svg viewBox="0 0 20 20"><rect x="2" y="4" width="16" height="12" fill="none" stroke="var(--yellow)" stroke-width="2"/><path d="M2 4 L10 11 L18 4" fill="none" stroke="var(--yellow)" stroke-width="2"/></svg>
      </li>
      <li>www.harborfilingreliefexperts.com
        <svg viewBox="0 0 20 20"><circle cx="10" cy="10" r="8" fill="none" stroke="var(--yellow)" stroke-width="2"/><ellipse cx="10" cy="10" rx="3.5" ry="8" fill="none" stroke="var(--yellow)" stroke-width="1.5"/><path d="M2 10 H18" stroke="var(--yellow)" stroke-width="1.5"/></svg>
      </li>
    </ul>
  </main>
</body>
</html>
```